New Packaging Design Project

Wine packaging redesign. Retail partner requested a redesign of a private label wine. The old label is attached. Our partner liked the Lantern and Briar label and wanted something similar. There will be a logo added to the top of the label

Went on vacation/holiday

```html
<!DOCTYPE html>
<html lang="en">
<head>
<meta charset="utf-8">
<title>Peaks and Tides Red Blend Label</title>
<link rel="stylesheet" href="https://fonts.googleapis.com/css2?family=Barlow+Condensed:wght@300;400;500&family=Cinzel:wght@400&display=swap">
<style>
  :root {
    --page-bg: #ffffff;
    --label-bg: #3a3a3c;
    --gold: #a88a22;
    --gold-deep: #3a2f0c;
    --text-light: #d6d6d6;
    --text-year: #e4e4e4;
    --scene-dark: #000000;
  }
  html, body {
    margin: 0;
    padding: 0;
    width: 1200px;
    height: 960px;
    overflow: hidden;
    background: var(--page-bg);
  }
  .canvas {
    position: relative;
    width: 1200px;
    height: 960px;
  }
  .label-shadow {
    position: absolute;
    left: 200px;
    top: 72px;
    width: 797px;
    height: 813px;
    filter: drop-shadow(18px 22px 26px rgba(0, 0, 0, 0.28));
  }
  .label {
    position: relative;
    width: 100%;
    height: 100%;
    background: var(--label-bg);
    clip-path: polygon(0 0, 100% 0, 97.1% 100%, 2.9% 100%);
    text-align: center;
    overflow: hidden;
  }
  .label__landscape {
    position: absolute;
    left: 0;
    right: 0;
    top: 520px;
    bottom: 0;
    background: linear-gradient(160deg,
      var(--scene-dark) 0%,
      var(--scene-dark) 30%,
      var(--gold-deep) 55%,
      var(--scene-dark) 75%,
      var(--gold-deep) 100%);
  }
  .label__name {
    position: absolute;
    top: 156px;
    left: 0;
    right: 0;
    margin: 0;
    font-family: "Cinzel", "Trajan Pro", serif;
    font-weight: 400;
    font-size: 76px;
    line-height: 1;
    color: var(--gold);
    text-transform: uppercase;
    white-space: nowrap;
  }
  .label__style {
    position: absolute;
    top: 293px;
    left: 0;
    right: 0;
    margin: 0;
    font-family: "Barlow Condensed", sans-serif;
    font-weight: 500;
    font-size: 44px;
    line-height: 1;
    color: var(--gold);
    text-transform: uppercase;
  }
  .label__rule {
    position: absolute;
    top: 357px;
    left: 50%;
    width: 32px;
    height: 3px;
    margin-left: -16px;
    background: var(--gold);
  }
  .label__varieties {
    position: absolute;
    top: 376px;
    left: 0;
    right: 0;
    margin: 0;
    font-family: "Barlow Condensed", sans-serif;
    font-weight: 300;
    font-size: 28px;
    line-height: 34px;
    color: var(--text-light);
    text-transform: uppercase;
  }
  .label__varieties .sep {
    padding: 0 14px;
  }
  .label__vintage {
    position: absolute;
    top: 472px;
    left: 0;
    right: 0;
    margin: 0;
    font-family: "Barlow Condensed", sans-serif;
    font-weight: 400;
    font-size: 30px;
    line-height: 1;
    color: var(--text-year);
  }
</style>
</head>
<body>
<main class="canvas">
  <div class="label-shadow">
    <article class="label">
      <div class="label__landscape" role="img" aria-label="Vineyard hills illustration with gold row lines and cypress trees"></div>
      <h1 class="label__name">Peaks and Tides</h1>
      <h2 class="label__style">Red Blend</h2>
      <div class="label__rule"></div>
      <p class="label__varieties">
        Merlot<span class="sep">|</span>Cabernet Sauvignon<br>
        Cabernet Franc<span class="sep">|</span>Petit Verdot<span class="sep">|</span>Malbec
      </p>
      <p class="label__vintage">2018</p>
    </article>
  </div>
</main>
</body>
</html>
```